Classic Minimalistic Business Card

Design a classic, minimalistic Business Card. Please find inspiration in the attached Classic Minimalistic examples. My information:
Name: Glen Ovamir
Company: Ovamir Capital
Logo: OC
Address: 1470 N Thornwick Rd, Suite 210 | Geneva, IL 60134
Phone: 630-555-0192
Email: glenovamir@pvt.insure
Slogan: Building Strength Through Capital

Feel free to leave out any of the information above except my name.

I have selected Double-sided, but I am also open to Single-sided

Target Market(s)

22-70. income greater than 150k/year

Industry/Entity Type

Finance

Contact Information for Business Card

See Project Description

Requirements
Must have
• Ivory or "antiqued" background similar to the reference pictures

```html
<!DOCTYPE html>
<html lang="en">
<head>
<meta charset="utf-8">
<title>Ovamir Capital — Business Card</title>
<link href="https://fonts.googleapis.com/css2?family=Oswald:wght@600&family=Poppins:wght@400;500;600&display=swap" rel="stylesheet">
<style>
  :root {
    --page: #ffffff;
    --ivory-light: #f7f4ec;
    --ivory-mid: #ece5d6;
    --ivory-edge: #d3c8b1;
    --ink: #141210;
    --ink-soft: #2a2724;
    --shadow: rgba(40, 32, 20, 0.28);
  }
  * { box-sizing: border-box; margin: 0; padding: 0; }
  html, body {
    width: 767px; height: 1200px; overflow: hidden;
    background: var(--page);
  }
  .sheet {
    width: 767px; height: 1200px;
    display: flex; flex-direction: column; align-items: center; justify-content: center;
    gap: 56px;
  }
  .card {
    position: relative;
    width: 640px; height: 366px;
    background:
      radial-gradient(ellipse 70% 65% at 50% 50%, var(--ivory-light) 0%, var(--ivory-mid) 62%, var(--ivory-edge) 100%);
    box-shadow: 0 14px 26px -10px var(--shadow), 0 2px 6px rgba(40,32,20,0.12);
    color: var(--ink);
    font-family: "Poppins", sans-serif;
  }
  /* Front */
  .card-front {
    display: flex; flex-direction: column; align-items: center; justify-content: center;
    padding-top: 40px;
  }
  .brand-name {
    font-family: "Poppins", sans-serif;
    font-weight: 500;
    font-size: 42px;
    letter-spacing: 0.5px;
    color: var(--ink);
    line-height: 1;
  }
  .slogan {
    margin-top: 16px;
    font-family: "Poppins", sans-serif;
    font-weight: 500;
    font-size: 11.5px;
    letter-spacing: 4px;
    text-transform: uppercase;
    color: var(--ink);
  }
  /* Back */
  .card-back { display: flex; align-items: center; }
  .brand-block {
    width: 330px;
    display: flex; flex-direction: column; align-items: center;
    padding-top: 70px;
  }
  .brand-block .brand-name { font-size: 32px; }
  .brand-block .slogan { font-size: 9px; letter-spacing: 3px; margin-top: 12px; }
  .contact-block { padding-left: 22px; padding-top: 10px; }
  .person-name {
    font-family: "Oswald", sans-serif;
    font-weight: 600;
    font-size: 29px;
    line-height: 1.05;
    color: var(--ink);
  }
  .company {
    font-size: 18px; font-weight: 400; color: var(--ink-soft);
    margin-top: 2px; margin-bottom: 14px;
  }
  .contact-list { list-style: none; }
  .contact-item {
    display: flex; align-items: flex-start; gap: 8px;
    font-size: 12.5px; line-height: 1.35; color: var(--ink-soft);
    margin-bottom: 3px;
  }
  .contact-item .icon { width: 11px; height: 11px; flex: none; margin-top: 3px; fill: var(--ink); }
  .address-item { font-size: 11px; line-height: 1.3; }
</style>
</head>
<body>
<main class="sheet">
  <section class="card card-front" aria-label="Card front">
    <div class="brand-name">Ovamir Capital</div>
    <div class="slogan">Building Strength Through Capital</div>
  </section>

  <section class="card card-back" aria-label="Card back">
    <div class="brand-block">
      <div class="brand-name">Ovamir Capital</div>
      <div class="slogan">Building Strength Through Capital</div>
    </div>
    <div class="contact-block">
      <div class="person-name">Glen Ovamir</div>
      <div class="company">Ovamir Capital</div>
      <ul class="contact-list">
        <li class="contact-item">
          <svg class="icon" viewBox="0 0 24 24" aria-hidden="true"><path d="M6.6 10.8a15.1 15.1 0 0 0 6.6 6.6l2.2-2.2a1 1 0 0 1 1-.25 11.4 11.4 0 0 0 3.6.57 1 1 0 0 1 1 1V20a1 1 0 0 1-1 1A17 17 0 0 1 3 4a1 1 0 0 1 1-1h3.5a1 1 0 0 1 1 1c0 1.25.2 2.45.57 3.57a1 1 0 0 1-.25 1z"/></svg>
          <span>630-555-0192</span>
        </li>
        <li class="contact-item">
          <svg class="icon" viewBox="0 0 24 24" aria-hidden="true"><path d="M2 5h20v14H2z M2 5l10 7 10-7" fill="none" stroke="currentColor"/><path d="M2 6.5V19h20V6.5l-10 7z M2.5 5h19L12 11.6z"/></svg>
          <span>glenovamir@pvt.insure</span>
        </li>
        <li class="contact-item address-item">
          <svg class="icon" viewBox="0 0 24 24" aria-hidden="true"><path d="M12 2a7 7 0 0 0-7 7c0 5.2 7 13 7 13s7-7.8 7-13a7 7 0 0 0-7-7zm0 9.5A2.5 2.5 0 1 1 12 6.5a2.5 2.5 0 0 1 0 5z"/></svg>
          <span>1470 N Thornwick Rd, Suite 210<br>Geneva, IL 60134</span>
        </li>
      </ul>
    </div>
  </section>
</main>
</body>
</html>
```